Bref créative
Business Cards and Stationery for The Cheerful Parcel
The Cheerful Parcel
Traditional
Nora Whitcomb
Chief Executive Officer
24817 Halvern
Dunmore, MI 4735-1186
nora@thecheerfulparcel.example
www.thecheerfulparcel.example
This is my logo in AI

```html
<!DOCTYPE html>
<html lang="en">
<head>
<meta charset="utf-8">
<title>The Cheerful Parcel – Business Card</title>
<link rel="stylesheet" href="https://fonts.googleapis.com/css2?family=Open+Sans:ital,wght@0,400;0,600;1,400&display=swap">
<style>
  :root {
    --backdrop: #d9d9d9;
    --card-purple: #6b1572;
    --pink: #f6b3ab;
    --pink-light: #fbd3cc;
    --accent-orange: #f39a6b;
    --white: #ffffff;
  }
  * { box-sizing: border-box; margin: 0; padding: 0; }
  html, body {
    width: 1200px; height: 895px; overflow: hidden;
    background: var(--backdrop);
    font-family: "Open Sans", Arial, sans-serif;
  }
  .canvas { position: relative; width: 1200px; height: 895px; }

  .card {
    position: absolute;
    width: 700px; height: 400px;
    background: var(--card-purple);
    box-shadow: 0 6px 18px rgba(0,0,0,0.18);
  }
  .card--back { left: 440px; top: 45px; }
  .card--front { left: 60px; top: 460px; }

  /* back side */
  .back-url {
    position: absolute; left: 40px; top: 230px;
    color: var(--white); font-size: 15px; letter-spacing: 2px;
  }
  .gift-art {
    position: absolute; right: 50px; top: 70px;
    width: 230px; height: 240px;
    background: linear-gradient(160deg, var(--pink-light), var(--pink));
    border-radius: 6px;
  }

  /* front side */
  .brand {
    position: absolute; left: 0; right: 0; top: 70px;
    text-align: center;
  }
  .brand-name {
    display: inline-flex; align-items: center; gap: 12px;
    color: var(--white); font-size: 40px; font-weight: 600;
  }
  .brand-dot {
    width: 22px; height: 22px; border-radius: 50%; background: var(--pink);
  }
  .tagline {
    margin-top: 10px;
    color: var(--pink); font-size: 15px; font-style: italic; letter-spacing: 1px;
  }
  .person {
    position: absolute; left: 0; right: 0; top: 222px;
    text-align: center; color: var(--accent-orange); font-size: 16px;
  }
  .person-name { font-weight: 600; }
  .contacts {
    position: absolute; left: 40px; right: 40px; bottom: 40px;
    color: var(--pink); font-size: 13px;
  }
  .contact-row { display: flex; justify-content: center; gap: 16px; margin-top: 8px; }
  .contact-item { display: inline-flex; align-items: center; gap: 6px; white-space: nowrap; }
  .contact-icon { width: 13px; height: 13px; flex: none; }
</style>
</head>
<body>
<main class="canvas">

  <section class="card card--back" aria-label="Card back">
    <p class="back-url">www.TheCheerfulParcel.example</p>
    <div class="gift-art" role="img" aria-label="Illustration of a pink gift box tied with a white ribbon bow"></div>
  </section>

  <section class="card card--front" aria-label="Card front">
    <div class="brand">
      <div class="brand-name"><span class="brand-dot"></span>The Cheerful Parcel</div>
      <p class="tagline">Bright parcels for every day</p>
    </div>

    <p class="person"><span class="person-name">Nora Whitcomb</span> / Chief Executive Officer</p>

    <div class="contacts">
      <div class="contact-row">
        <span class="contact-item">
          <svg class="contact-icon" viewBox="0 0 12 12"><circle cx="6" cy="6" r="6" fill="var(--accent-orange)"/><path d="M6 2.5a2.2 2.2 0 0 0-2.2 2.2C3.8 6.5 6 9.5 6 9.5s2.2-3 2.2-4.8A2.2 2.2 0 0 0 6 2.5z" fill="var(--white)"/></svg>
          24817 Halvern Dunmore, MI 4735-1186
        </span>
        <span class="contact-item">
          <svg class="contact-icon" viewBox="0 0 12 12"><circle cx="6" cy="6" r="6" fill="var(--accent-orange)"/><path d="M4 3l1.2 1.4-.6.9a5 5 0 0 0 2.1 2.1l.9-.6L9 8l-.8 1C5.5 9 3 6.5 3 3.8z" fill="var(--white)"/></svg>
          734-555-0142
        </span>
        <span class="contact-item">
          <svg class="contact-icon" viewBox="0 0 12 12"><circle cx="6" cy="6" r="6" fill="var(--accent-orange)"/><rect x="4" y="2.5" width="4" height="7" rx="0.8" fill="var(--white)"/></svg>
          3135550186
        </span>
      </div>
      <div class="contact-row">
        <span class="contact-item">
          <svg class="contact-icon" viewBox="0 0 12 12"><circle cx="6" cy="6" r="6" fill="var(--accent-orange)"/><path d="M4 3l1.2 1.4-.6.9a5 5 0 0 0 2.1 2.1l.9-.6L9 8l-.8 1C5.5 9 3 6.5 3 3.8z" fill="var(--white)"/></svg>
          734-555-0177
        </span>
        <span class="contact-item">
          <svg class="contact-icon" viewBox="0 0 12 12"><circle cx="6" cy="6" r="6" fill="var(--accent-orange)"/><rect x="3" y="4" width="6" height="4.2" fill="var(--white)"/><path d="M3 4l3 2.3L9 4" stroke="var(--accent-orange)" stroke-width="0.7" fill="none"/></svg>
          nora@thecheerfulparcel.example
        </span>
        <span class="contact-item">
          <svg class="contact-icon" viewBox="0 0 12 12"><circle cx="6" cy="6" r="6" fill="var(--accent-orange)"/><circle cx="6" cy="6" r="3" stroke="var(--white)" stroke-width="0.8" fill="none"/><path d="M3 6h6M6 3v6" stroke="var(--white)" stroke-width="0.6"/></svg>
          www.thecheerfulparcel.example
        </span>
      </div>
    </div>
  </section>

</main>
</body>
</html>
```